Medical IT Business with New logo needs a fresh stationary design

First time on sketch Harbor; Thought I would give it a go.
This project is for business cards alone but we have loads of design work that needs to take place in the immediate future.

We provide IT services to the Medical Industry and value ourselves as offering a premium product to the market.

I am after a fresh, clean design using full colour 2 sided cards which includes our current colour palettes from our logo.

Card's must include:
- Logo
- Slogan
- Name
- Adress
- Email
- Phone
- Fax
- Mobile

Target Market(s)

Surgeons, High Profile Medical Personnel

Industry/Entity Type

Business

Fonts, CMYK Colours and Logo files attached.

Requirements
Must have
• Card's must include:
• - Logo
• - Slogan
• - Name
• - Adress
• - Email
• - Phone
• - Fax
• - Mobile
Nice to have
• Needs to incorporate our colour palette (attached CMYK colours)
Should not have
• Black backgrounds. Black text ok.

```html
<!DOCTYPE html>
<html lang="en">
<head>
<meta charset="utf-8">
<title>Caremesh Systems – Business Cards</title>
<link rel="stylesheet" href="https://fonts.googleapis.com/css2?family=Lato:wght@400;700;900&display=swap">
<style>
  :root {
    --backdrop: #e9ecef;
    --brand-blue: #1487c2;
    --brand-blue-deep: #0a6a9e;
    --navy: #0f3d6e;
    --ink: #1d2530;
    --paper: #ffffff;
    --paper-shade: #f1f3f5;
    --map-tone: rgba(200, 208, 217, .75);
    --map-tint: rgba(196, 222, 240, .85);
  }
  * { box-sizing: border-box; margin: 0; padding: 0; }
  html, body {
    width: 1200px; height: 873px; overflow: hidden;
    background: var(--backdrop);
    font-family: "Lato", Arial, sans-serif;
  }
  .stage { position: relative; width: 1200px; height: 873px; }

  .card {
    position: absolute; width: 520px; height: 300px;
    border-radius: 18px; overflow: hidden;
    box-shadow: 0 14px 30px rgba(0,0,0,.18);
  }

  /* Front */
  .card--front {
    left: 50px; top: 200px;
    background: linear-gradient(160deg, var(--brand-blue) 0%, var(--brand-blue-deep) 100%);
  }
  .front-brand {
    position: absolute; left: 60px; top: 95px;
    display: flex; align-items: center; gap: 22px;
  }
  .front-brand .brand-dot {
    width: 110px; height: 110px; border-radius: 50%; background: var(--paper); flex: none;
  }
  .front-brand .brand-name {
    color: var(--paper); font-weight: 900; font-size: 34px; line-height: 1.02; letter-spacing: 1px;
  }
  .front-brand .slogan {
    color: var(--paper); font-weight: 400; font-size: 15px; margin-top: 6px; opacity: .9;
  }

  /* Back */
  .card--back {
    left: 630px; top: 373px;
    background: linear-gradient(170deg, var(--paper) 0%, var(--paper-shade) 100%);
  }
  .world-map {
    position: absolute; left: 40px; top: 20px; width: 440px; height: 210px;
    background: radial-gradient(closest-side at 55% 50%, var(--map-tint) 0%, var(--map-tone) 50%, rgba(200,208,217,0) 100%);
  }
  .back-brand {
    position: absolute; left: 30px; top: 150px;
    display: flex; align-items: center; gap: 12px;
  }
  .back-brand .brand-dot {
    width: 56px; height: 56px; border-radius: 50%; background: var(--brand-blue); flex: none;
  }
  .back-brand .brand-name {
    color: var(--navy); font-weight: 900; font-size: 21px; line-height: 1.05; letter-spacing: .5px;
  }
  .back-brand .slogan {
    color: var(--brand-blue); font-size: 11px; margin-top: 3px;
  }
  .divider {
    position: absolute; left: 268px; top: 50px; width: 2px; height: 130px;
    background: linear-gradient(180deg, rgba(20,135,194,0) 0%, var(--brand-blue) 50%, rgba(20,135,194,0) 100%);
  }
  .contact {
    position: absolute; left: 285px; top: 52px;
  }
  .contact .person-name { color: var(--navy); font-weight: 700; font-size: 19px; }
  .contact .person-role { color: var(--ink); font-size: 12px; margin-top: 1px; }
  .contact-list { list-style: none; margin-top: 18px; }
  .contact-list li {
    display: flex; align-items: center; gap: 10px;
    color: var(--ink); font-size: 14px; margin-bottom: 6px;
  }
  .contact-list svg { width: 16px; height: 14px; fill: var(--navy); flex: none; }
  .address {
    position: absolute; left: 0; right: 0; bottom: 26px; text-align: center;
    color: var(--brand-blue); font-weight: 700; font-size: 17px;
  }
</style>
</head>
<body>
<main class="stage">

  <section class="card card--front" aria-label="Card front">
    <div class="front-brand">
      <span class="brand-dot"></span>
      <div>
        <div class="brand-name">CAREMESH<br>SYSTEMS</div>
        <div class="slogan">connected care for clinics</div>
      </div>
    </div>
  </section>

  <section class="card card--back" aria-label="Card back">
    <div class="world-map" role="img" aria-label="Faint dotted world map background"></div>

    <div class="back-brand">
      <span class="brand-dot"></span>
      <div>
        <div class="brand-name">CAREMESH<br>SYSTEMS</div>
        <div class="slogan">connected care for clinics</div>
      </div>
    </div>

    <div class="divider"></div>

    <div class="contact">
      <div class="person-name">Daniel Whitcombe</div>
      <div class="person-role">Chief Operating Officer</div>
      <ul class="contact-list">
        <li>
          <svg viewBox="0 0 16 14" aria-label="Phone"><path d="M1 4c0-2 2-3 7-3s7 1 7 3v1h-4V4H5v1H1z"/><rect x="3" y="6" width="10" height="7" rx="1.5"/></svg>
          555-014-2280
        </li>
        <li>
          <svg viewBox="0 0 16 14" aria-label="Fax"><rect x="4" y="0" width="8" height="4"/><rect x="1" y="4" width="14" height="6" rx="1"/><rect x="4" y="9" width="8" height="5"/></svg>
          555-014-2281
        </li>
        <li>
          <svg viewBox="0 0 16 14" aria-label="Email"><path d="M0 2h16v10H0z M1.5 3.5 8 8l6.5-4.5" stroke="#fff" stroke-width="1"/></svg>
          hello@caremeshsystems.com
        </li>
      </ul>
    </div>

    <div class="address">48 Alder Lane, Fairbrook, PA 10000</div>
  </section>

</main>
</body>
</html>
```